Coral Journey Mate - A Travel Services Website

Sunreef Home Rentals is a company that provides travels services to home owners and travellers to Barbados. Coral Journey Mate is a particular brand targeting travelling guests with specific set of travel services. The brand slogan is:

'Getting you the best for less'

The travel services will include:

- Coral Journey Mate Perks Pass
- Car Hire Quote Service
- Mobile Phone Sim Cards
- Prepaid Debit Cards
- Airport Hotel Booking
- Airport Lounge Booking
- Airport Parking

There will also be a travel planner function for guests.

The main puropse of the site is as follows:

1. Registration for the Coral Journey Mate Perks Pass

2. Creation of user account which the guest will frequently return to check for updates

3. Purchase of ancillary travel products and services

4. To use the Travel Planner

5. To gather data on holiday home owners in Barbados

A site map can be seen at the following link:

http://plotgridly.example/outlines/viewMap/4kqzvbn8ytrwpa2fuh5ximc07jldg6sqenoa9rvb33kf2pyq71

Webpage templates (2 required)

The first will be form control heavy (text boxes, checkboxes ect). It will need failure and success messages / indicators etc.

The second will be a general content area with a secondary navigation area (i.e for sub sections of the current section). This will house text / headings and images.

Both will require header, primary navigation, content and footer areas.

N.B. Please not that I am not technical and the above webtemplate narrative has been supplied by my web developer/programmer. If you have any questions, please ask me any questions and I will get an answer from him.

Target Market(s)

My customers tend to be:

Sex: Female
Age: 24-55
Location: UK, USA, Canada
Social Class: A,B,C1
Income: Medium income bracket

They are possibly visiting Barbados for the first and only time. It is an expensive destination and is accessible to people with a medium to high income. They still desire 'value for money'. Therefore the sight must give guests confidence that Coral Journey Mate is 'their friend', is seeking to offer the best value deals for their vacation/holiday.

Industry/Entity Type

Travel

Requirements
Must have
• The site templates must be professional, aspirational, trustworthy, reassuring, clean, innovative, fun. When people visit the site they should be excited about the savings that they can make and want to return as there is a perceived benefit for them. It must look expensive and professional in its projected image.
Nice to have
• Smooth currved lines, seperated boxed areas for content, as simple and uncluttered layout and it must be simple to read!
Should not have
• It should not be cartoonly, despite my attached logo and must not look cheap.

```html
<!DOCTYPE html>
<html lang="en">
<head>
<meta charset="utf-8">
<title>Coral Journey Mate – Account Settings</title>
<link href="https://fonts.googleapis.com/css2?family=Great+Vibes&family=Oswald:wght@400;500&family=Open+Sans:wght@400;600;700&family=Arimo:wght@400;700&display=swap" rel="stylesheet">
<style>
:root{
  --sky-deep:#0b3f9e;
  --sky:#1f77c9;
  --sea:#3fc0e6;
  --sand:#e9d8b9;
  --orange:#f26a1b;
  --orange-dark:#d9420c;
  --red:#e32b2b;
  --crimson:#d91a2a;
  --blue:#0fa3dd;
  --navy:#0d3b5a;
  --yellow:#fde79a;
  --gold:#f4a623;
  --grey-box:#f0f0f0;
  --line:#cfcfcf;
  --white:#fff;
}
*{box-sizing:border-box;margin:0;padding:0}
html,body{width:939px;height:1200px;overflow:hidden;background:#fff}
body{font-family:"Open Sans",sans-serif;color:var(--navy)}
.page{position:relative;width:939px;height:1200px;overflow:hidden}
.abs{position:absolute}

/* header */
.hero-scene{left:0;top:0;width:939px;height:494px;
  background:linear-gradient(180deg,var(--sky-deep) 0%,var(--sky) 30%,#5fb6e8 45%,var(--sea) 62%,#69d0ea 80%,var(--sand) 100%)}
.brand{left:34px;top:52px;display:flex;align-items:center;gap:12px}
.brand-dot{width:54px;height:54px;border-radius:50%;background:var(--red)}
.brand-name{font-family:"Oswald",sans-serif;font-weight:500;font-size:38px;line-height:1;color:var(--white);width:240px}
.call{right:38px;top:60px;text-align:right;color:var(--white)}
.call-label{font-family:"Great Vibes",cursive;font-size:48px;line-height:1;color:var(--red)}
.call-number{font-family:"Oswald",sans-serif;font-size:28px;letter-spacing:1px;margin-top:2px}

/* nav */
.nav{left:19px;top:182px;width:900px;height:38px;border-radius:10px;
  background:linear-gradient(180deg,#ff8a3d,var(--orange) 50%,var(--orange-dark));display:flex;align-items:center;
  font-family:"Arimo",sans-serif;font-size:14px;color:var(--white)}
.nav a{color:inherit;text-decoration:none;height:38px;display:flex;align-items:center;padding:0 21px;border-right:1px solid rgba(255,255,255,.25)}
.nav a.active{background:var(--blue);color:#0b2d4a;border-radius:10px 0 0 10px;padding:0 22px 0 24px}
.signin{position:absolute;right:50px;top:9px;display:flex;align-items:center;gap:8px}
.signin input{width:109px;height:19px;border-radius:4px;border:1px solid #ddd;background:#fafafa;font-size:10px;padding:0 6px;color:#aaa}
.signin button{width:63px;height:20px;border-radius:4px;border:0;background:linear-gradient(#7fd6ff,#18a3e3);font:700 11px "Arimo",sans-serif;color:#0b2d4a}

/* hero panel */
.promo{left:19px;top:233px;width:901px;height:247px;border-radius:14px;background:rgba(80,200,235,.7)}
.promo-title{left:46px;top:20px;font-family:"Great Vibes",cursive;font-size:37px;color:var(--white);line-height:1}
.promo-sub{left:158px;top:57px;font-family:"Great Vibes",cursive;font-size:22px;line-height:1.1;color:var(--crimson)}
.promo-copy{left:44px;top:85px;width:400px;font-size:10.3px;line-height:16px;color:var(--crimson)}
.btn{display:flex;align-items:center;justify-content:space-between;border-radius:14px;
  background:linear-gradient(#ffe27a,var(--gold));font-family:"Oswald",sans-serif;font-weight:500;font-size:15px;color:#222;padding:0 8px 0 12px}
.btn .go{width:22px;height:22px}
.apply{left:44px;top:192px;width:134px;height:30px}
.cards{left:490px;top:12px;width:400px;height:222px}

/* content shell */
.shell{left:18px;top:511px;width:903px;height:600px;border:2px solid #e6e6e6;border-radius:14px;background:#fff}
.side-title{left:30px;top:530px;font-family:"Oswald",sans-serif;font-size:16px;line-height:20px;color:var(--red)}
.side-user{left:31px;top:552px;font-family:"Oswald",sans-serif;font-size:13px;line-height:16px;color:var(--blue)}
.menu{left:29px;top:581px;width:232px;height:161px;border-radius:9px;background:linear-gradient(var(--yellow),var(--gold));padding:9px 10px 0 8px;list-style:none}
.menu li{height:28px;display:flex;align-items:center;gap:8px;font-size:11px;font-weight:700;color:#3a2506;border-bottom:1px dashed rgba(120,80,10,.35)}
.menu li::before{content:"";width:10px;height:8px;background:repeating-conic-gradient(#222 0 25%,transparent 0 50%) 0 0/5px 4px}
.register{left:29px;top:753px;width:232px;height:96px;border-radius:9px;overflow:hidden;background:var(--red)}
.register .top{height:49px;background:linear-gradient(#ff7a60,#f04a3a);padding:6px 9px;font-family:"Oswald",sans-serif;line-height:1}
.register .q{font-family:"Open Sans",sans-serif;font-size:14px;color:#5a1b10}
.register .brandline{font-size:19px;color:#fff}
.register .cta{padding:11px 8px;font-family:"Oswald",sans-serif;font-size:21px;color:#fff;display:flex;gap:12px;align-items:center}
.planner{left:29px;top:859px;width:232px;height:239px;border-radius:9px;background:#fbe8b2;overflow:hidden}
.planner-head{height:44px;background:linear-gradient(#63bde9,#2e94d0);color:#fff;font-family:"Oswald",sans-serif;font-size:17px;padding:10px 14px}
.calendar{position:absolute;left:5px;top:47px;width:222px;height:184px;border-radius:8px;background:#8a7565;padding:5px 9px}
.cal-label{font-size:11px;font-weight:700;color:#fff;margin-bottom:6px}
.cal-body{background:#fdf0c6;border-radius:6px;height:147px;padding:4px 4px 0}
.cal-month{height:23px;border-radius:6px;background:linear-gradient(#ffdf8a,var(--gold));display:flex;align-items:center;justify-content:space-between;padding:0 6px;font-size:11px;font-weight:700;color:#3a2506}
.cal-month i{width:11px;height:11px;border-radius:50%;background:#3a2506}
.cal-grid{display:grid;grid-template-columns:repeat(7,29px);row-gap:5px;margin-top:5px;font-size:11px;font-weight:700;text-align:center}
.cal-grid .dn{color:var(--crimson)}
.cal-grid .d{width:21px;height:16px;margin:0 auto;background:linear-gradient(#ffb347,#ef8a16);color:#3a1a05;line-height:16px}

/* form */
.h-red{font-family:"Oswald",sans-serif;font-size:16px;line-height:20px;color:var(--red)}
.h-blue{font-family:"Arimo",sans-serif;font-size:13.5px;line-height:16px;color:var(--blue)}
.fbox{left:286px;width:611px;border-radius:10px;background:linear-gradient(#fff,var(--grey-box))}
.row{position:absolute;left:0;width:801px;display:flex;align-items:center;height:17px}
.row label{width:535px;text-align:right;font-size:11px;font-weight:700}
.row .inp{position:absolute;left:554px;width:247px;height:17px;border:1px solid var(--line);background:linear-gradient(#fff,#ececec)}
.row .inp.s{width:79px}
.opt{position:absolute;left:0;width:760px;text-align:right;font-size:11px;line-height:14px;font-weight:700;white-space:nowrap}
.tick{position:absolute;left:776px;width:11px;height:11px;border:1px solid #888;background:#fff}
.submit{left:554px;top:1066px;width:121px;height:29px}

/* footer */
.footer{left:0;top:1124px;width:939px;height:76px;background:linear-gradient(#ff6a20,var(--orange-dark));display:flex;align-items:center;justify-content:center;gap:10px;font-size:11px;color:#fff}
</style>
</head>
<body>
<div class="page">

  <div class="abs hero-scene" role="img" aria-label="Tropical beach photo with palm trees, turquoise sea and blue sky"></div>

  <div class="abs brand">
    <span class="brand-dot"></span>
    <span class="brand-name">Coral Journey Mate</span>
  </div>

  <div class="abs call">
    <div class="call-label">Call Us</div>
    <div class="call-number">555.0147.0199</div>
  </div>

  <nav class="abs nav">
    <a class="active">Home</a><a>About Us</a><a>Services</a><a>Products</a><a>Contact Us</a>
    <div class="signin">
      <span>Sign In</span>
      <input placeholder="user id"><input placeholder="password">
      <button>Sign In</button>
    </div>
  </nav>

  <section class="abs promo">
    <div class="abs promo-title">Getting You The best For Less</div>
    <div class="abs promo-sub">Coral Journey Mate Perks Pass</div>
    <p class="abs promo-copy">Vivamus mattis odio ut arcu malesuada vehicula. Pellentesque nec massa quis turpis ornare aliquet a venenatis neque. Aenean fermentum eros sit amet nulla sagittis quis venenatis ipsum convallis.<br>Vivamus mattis odio ut arcu malesuada vehicula. Pellentesque nec massa quis turpis ornare aliquet a venenatis neque. Aenean fermentum eros sit amet nulla sagittis quis venenatis ipsum convallis.</p>
    <div class="abs btn apply">APPLY NOW!
      <svg class="go" viewBox="0 0 22 22"><circle cx="11" cy="11" r="10" fill="#e8362a"/><path d="M6 11h9M11 7l4 4-4 4" stroke="#fff" stroke-width="2" fill="none"/></svg>
    </div>
    <svg class="abs cards" viewBox="0 0 400 222" role="img" aria-label="Photo of two membership perks pass cards">
      <rect x="30" y="30" width="210" height="140" rx="12" transform="rotate(-18 135 100)" fill="#bfe3f2" stroke="#2a5d7a" stroke-width="2"/>
      <rect x="150" y="40" width="240" height="155" rx="12" transform="rotate(-18 270 118)" fill="#eaf6fc" stroke="#2a5d7a" stroke-width="2"/>
    </svg>
  </section>

  <div class="abs shell"></div>

  <aside>
    <div class="abs side-title">ACCOUNT DASHBOARD</div>
    <div class="abs side-user">XXXX XXXXXX</div>
    <ul class="abs menu">
      <li>Home</li><li>Preparation List</li><li>Get A Perks Pass</li><li>Get Car Hire</li><li>Settings</li>
    </ul>
    <div class="abs register">
      <div class="top"><div class="q">Are You new to</div><div class="brandline">CORAL JOURNEY MATE</div></div>
      <div class="cta">SIGN UP / REGISTER
        <svg width="28" height="12" viewBox="0 0 28 12"><path d="M1 1l5 5-5 5M10 1l5 5-5 5M19 1l5 5-5 5" stroke="#fff" stroke-width="2.5" fill="none"/></svg>
      </div>
    </div>
    <div class="abs planner">
      <div class="planner-head">BARBADOS TRAVEL PLANNER</div>
      <div class="calendar">
        <div class="cal-label">Specific Date</div>
        <div class="cal-body">
          <div class="cal-month"><i></i>Septembe, 2010<i></i></div>
          <div class="cal-grid">
            <span class="dn">Su</span><span class="dn">Mo</span><span class="dn">Tu</span><span class="dn">We</span><span class="dn">Th</span><span class="dn">Fr</span><span class="dn">Sa</span>
            <span></span><span></span><span class="d">1</span><span class="d">2</span><span class="d">3</span><span class="d">4</span><span class="d">5</span>
            <span class="d">6</span><span class="d">7</span><span class="d">8</span><span class="d">9</span><span class="d">10</span><span class="d">11</span><span class="d">12</span>
            <span class="d">13</span><span class="d">14</span><span class="d">15</span><span class="d">16</span><span class="d">17</span><span class="d">18</span><span class="d">19</span>
            <span class="d">20</span><span class="d">21</span><span class="d">22</span><span class="d">23</span><span class="d">24</span><span class="d">25</span><span class="d">26</span>
            <span class="d">27</span><span class="d">28</span><span class="d">29</span><span class="d">30</span>
          </div>
        </div>
      </div>
    </div>
  </aside>

  <main>
    <div class="abs h-red" style="left:288px;top:530px">ACCOUNT SETTINGS</div>
    <div class="abs h-blue" style="left:289px;top:553px">YOUR DETAILS</div>
    <div class="abs fbox" style="top:583px;height:79px"></div>
    <div class="row" style="top:588px"><label>Email Address:</label><span class="inp"></span></div>
    <div class="row" style="top:610px"><label>Password:</label><span class="inp"></span></div>
    <div class="row" style="top:633px"><label>Confirm Password:</label><span class="inp"></span></div>

    <div class="abs h-blue" style="left:289px;top:673px">PERSONAL DETAILS</div>
    <div class="abs fbox" style="top:696px;height:266px"></div>
    <div class="row" style="top:702px"><label>First Name:</label><span class="inp"></span></div>
    <div class="row" style="top:725px"><label>Last Name:</label><span class="inp"></span></div>
    <div class="row" style="top:760px"><label>House Number / Street:</label><span class="inp"></span></div>
    <div class="row" style="top:783px"><label>Address Line 2:</label><span class="inp"></span></div>
    <div class="row" style="top:806px"><label>Town:</label><span class="inp"></span></div>
    <div class="row" style="top:828px"><label>Country:</label><span class="inp"></span></div>
    <div class="row" style="top:851px"><label>Postcoide:</label><span class="inp"></span></div>
    <div class="row" style="top:873px"><label>Country:</label><span class="inp"></span></div>
    <div class="row" style="top:904px"><label>Phone:</label><span class="inp"></span></div>
    <div class="row" style="top:927px"><label>Departure Date:</label><span class="inp s"></span><span class="inp s" style="left:638px"></span><span class="inp s" style="left:722px"></span></div>

    <div class="abs h-blue" style="left:288px;top:971px">ACCOUNT OPTION</div>
    <div class="abs fbox" style="top:992px;height:60px"></div>
    <div class="opt" style="top:1003px">Receive weekly email updates for your to - do list :</div>
    <svg class="tick" style="top:1004px" viewBox="0 0 11 11"><path d="M2 5l3 3 5-7" stroke="#222" stroke-width="1.8" fill="none"/></svg>
    <div class="opt" style="top:1025px">Opt - in to receive Selected Offers:</div>
    <span class="tick" style="top:1026px"></span>

    <div class="abs btn submit">SUBMIT
      <svg class="go" viewBox="0 0 22 22"><circle cx="11" cy="11" r="10" fill="#e8362a"/><path d="M6 11h9M11 7l4 4-4 4" stroke="#fff" stroke-width="2" fill="none"/></svg>
    </div>
  </main>

  <footer class="abs footer">
    <span>© Copyright</span><span>|</span><span>All Right Reserved</span><span>|</span><span>Privacy Policy</span><span>|</span><span>terms &amp; Conditions</span>
  </footer>
</div>
</body>
</html>
```